KU Curiosities

We need a web design for an ecommerce website that sells innovative gadgets. ***We are in the early stages of the business and don't have official products yet, they are being created. so we need to use placeholders and fake content, please email me with any questions regarding this.

The web page must look modern, fresh and simple and include-

• Logo
• My Account & View Cart link
• Menu - Home, Shop, The Latest, About Us, FAQ, Blog, Contact Us
• Promo bar at the top of the page like on: http://www.plumandwren.example/plwr/ (you can use placeholder text for now)
• Search Box
• Chatterpage, Chirpline, Vidstream, Clipboardly and Orbnet+ icons
• Slogan “Amaze your friends”
• Free shipping on orders over $50
• Banner section - for now you can highlight one of the fake products below, focus on free shipping on order over $50 or some kind of fake promotion
• New Arrivals section - highlight these fake products since we don't have products yet so you can use these products as place holders-
1. https://www.brisketbay.example/tech-gadgets/the-vorntap
2. https://www.brisketbay.example/tech-gadgets/lobelatch-earbud-securer
3. https://www.brisketbay.example/tech-gadgets/pestavo-headfoams
• credit card logos
• paytrellis.example seal - https://check.paytrellis.example/ptseal/images/secure90x72.gif

Example websites:
http://www.plumandwren.example/plwr/
https://www.brisketbay.example/
http://www.tinmantles.example/
https://sproutwell.example/
http://zevrodesk.example/
http://www.dallowsco.example/
http://www.vistaframe.example/

Requirements
Must have
• • Logo
• Search Box
• credit card logos

```html
<!DOCTYPE html>
<html lang="en">
<head>
<meta charset="utf-8">
<title>KU Curiosities — Innovative Gadgets</title>
<link href="https://fonts.googleapis.com/css2?family=Open+Sans:wght@400;600;700;800&display=swap" rel="stylesheet">
<style>
:root{
  --navy:#0c2556;
  --blue:#3aa8e0;
  --orange:#f7941d;
  --orange-dark:#e8761a;
  --red:#e0251b;
  --ink:#333;
  --muted:#777;
  --light:#999;
  --line:#e3e3e3;
  --panel:#efefef;
  --footer:#2b2b2b;
  --white:#fff;
}
*{box-sizing:border-box;margin:0;padding:0}
html,body{width:1200px;height:2185px;overflow:hidden;background:var(--white)}
body{font-family:"Open Sans",Arial,sans-serif;color:var(--ink);position:relative;font-size:12px}
.abs{position:absolute}
a{color:inherit;text-decoration:none}

/* promo bar */
.promo-bar{left:0;top:0;width:1200px;height:28px;background:var(--navy);color:var(--white);font-size:11.5px;font-weight:700;text-align:center;line-height:28px;white-space:nowrap}

/* header */
.site-header{left:0;top:28px;width:1200px;height:94px;background:var(--white)}
.logo{left:158px;top:22px;display:flex;align-items:center;gap:7px}
.logo-mark{width:26px;height:26px;border-radius:50%;background:var(--blue)}
.logo-name{font-size:14px;font-weight:700;color:var(--navy);line-height:1;white-space:nowrap}
.prefs{left:316px;top:16px;font-size:11px;color:var(--muted);display:flex;gap:26px;white-space:nowrap}
.prefs b{font-weight:400;color:var(--blue)}
.account-links{left:816px;top:16px;font-size:11px;color:var(--muted);display:flex;gap:6px;white-space:nowrap}
.account-links span{color:#bbb}
.main-nav{left:318px;top:62px;display:flex;font-size:13px;font-weight:600;color:#222;white-space:nowrap}
.main-nav a{padding:0 12px}
.main-nav a.active{color:var(--blue)}
.search-btn{left:952px;top:52px;width:28px;height:28px;border-radius:50%;background:var(--blue)}
.cart-btn{left:990px;top:52px;width:28px;height:28px;border-radius:4px;background:var(--blue)}
.cart-count{left:1026px;top:59px;font-size:11px;color:var(--muted)}

/* hero */
.hero{left:0;top:122px;width:1200px;height:510px;background:linear-gradient(90deg,#d6d1cd 0%,#a8998f 28%,#7d6557 50%,#4a3c37 72%,#6f6159 100%);border-bottom:2px solid var(--navy)}
.hero-title{left:0;top:182px;width:1200px;text-align:center;font-size:50px;font-weight:800;color:var(--white);line-height:1}
.hero-title span{color:var(--blue)}
.hero-sub{left:0;top:235px;width:1200px;text-align:center;font-size:27px;font-weight:600;color:var(--white);line-height:1}
.hero-sub span{color:var(--red)}
.hero-cta{left:475px;top:286px;width:226px;height:49px;border-radius:6px;background:linear-gradient(var(--orange),var(--orange-dark));color:var(--white);font-size:25px;font-weight:800;text-align:center;line-height:49px}
.hero-arrow{top:213px;width:44px;height:44px;border-radius:50%;background:rgba(60,60,60,.55);border:2px solid rgba(255,255,255,.8)}

/* shipping strip */
.ship-strip{left:146px;top:646px;width:908px;height:70px;background:#e9e9e9}
.ship-tag{left:0;top:0;width:140px;height:70px}
.ship-text{left:138px;top:0;line-height:70px;font-size:18.5px;color:#222;white-space:nowrap}

/* promo tiles */
.tile{top:737px;width:288px;height:163px;border:1px solid var(--line);overflow:hidden}
.tile-photo{position:absolute;top:0;height:100%}
.tile-1-text{left:10px;top:44px;font-size:16px;color:var(--blue);line-height:1.35}
.tile-btn{left:10px;top:100px;width:78px;height:26px;background:var(--orange);color:var(--white);font-size:10.5px;text-align:center;line-height:26px}
.tile-2-text{left:24px;top:44px;font-size:16px;font-weight:700;color:#222;line-height:1.35}
.tile-3-big{left:20px;top:68px;font-size:32px;font-weight:800;color:var(--orange);line-height:1}
.tile-3-big sup{font-size:11px;font-weight:700;vertical-align:top}
.tile-3-text{left:22px;top:108px;font-size:10px;color:var(--muted);width:110px;line-height:1.35}

/* new arrivals */
.section-title{left:146px;top:928px;font-size:17px;font-weight:700;color:#222}
.section-rule{left:146px;top:956px;width:908px;height:1px;background:var(--line)}
.pager{top:923px;width:26px;height:26px;border-radius:50%}
.card{width:218px;height:277px;border:1px solid var(--line);background:var(--white);overflow:hidden}
.card-photo{position:absolute;left:10px;top:10px;width:196px;height:255px}
.card-flag{left:0;top:0;width:0;height:0;border-top:70px solid var(--navy);border-right:70px solid transparent}
.card-flag.blue{border-top-color:var(--blue)}
.flag-text{color:var(--white);font-size:9px;font-weight:700;transform:rotate(-45deg);white-space:nowrap}
.card-hover{left:146px;top:980px;width:218px;height:340px;background:var(--white);box-shadow:0 2px 10px rgba(0,0,0,.22);z-index:3}
.price-badge{left:72px;top:172px;width:72px;height:72px;border-radius:50%;background:var(--orange);color:var(--white);font-size:16px;font-weight:700;text-align:center;line-height:72px}
.hover-name{left:0;top:252px;width:218px;text-align:center;font-size:12px;color:#222}
.stars{left:0;top:270px;width:218px;text-align:center;font-size:11px;color:var(--orange);letter-spacing:1px}
.hover-rule{left:0;top:290px;width:218px;height:1px;background:var(--line)}
.add-cart{left:14px;top:306px;font-size:10.5px;color:#555;display:flex;align-items:center;gap:6px}
.add-links{left:114px;top:300px;font-size:9.5px;color:#555;line-height:1.6;border-left:1px solid var(--line);padding-left:8px}

/* social row */
.col-title{font-size:15px;font-weight:600;color:#222}
.vrule{width:1px;background:var(--line)}
.tweet{left:153px;width:280px;display:flex;gap:12px}
.tweet-dot{flex:none;width:24px;height:24px;border-radius:50%;background:var(--blue);margin-top:2px}
.tweet-body{font-size:10.5px;color:#444;line-height:1.75}
.tweet-body b{font-weight:400;font-style:italic;color:var(--blue)}
.tweet-time{display:block;text-align:right;color:var(--light);font-size:9.5px}
.follow{left:195px;top:1855px;font-size:10px;color:var(--blue);border-top:1px solid var(--line);padding-top:6px;width:220px}
.like-row{left:485px;top:1635px;font-size:10.5px;color:#555;display:flex;align-items:center;gap:8px;white-space:nowrap}
.like-btn{border:1px solid #c7cfdd;background:#eef1f6;font-size:10px;font-weight:700;color:#3b5998;padding:2px 6px;border-radius:2px}
.like-row b{font-weight:600;color:var(--navy)}
.fan{width:52px;text-align:center;font-size:9.5px;color:#555}
.fan-photo{width:52px;height:50px;border:1px solid #ddd;background:linear-gradient(#b8a89c,#7e6e64);margin-bottom:4px}
.plugin{left:485px;top:1865px;font-size:10px;color:#555;display:flex;align-items:center;gap:6px}
.plugin i{width:12px;height:12px;background:#3b5998;display:block}
.about-text{left:794px;top:1634px;width:262px;font-size:10.5px;line-height:1.8;color:#444}
.contact-row{left:794px;display:flex;gap:14px;align-items:flex-start;font-size:10.5px;color:#444;line-height:1.55}
.contact-icon{flex:none;width:22px;height:22px;border-radius:3px;background:var(--blue)}

/* footer */
.footer{left:0;top:1940px;width:1200px;height:194px;background:var(--panel);border-top:1px solid #e0e0e0}
.fcol{top:36px}
.fcol h4{font-size:13px;font-weight:600;color:#222;margin-bottom:12px;border-bottom:1px solid #ddd;padding-bottom:8px;width:150px}
.fcol ul{list-style:none;font-size:10.5px;color:#444;line-height:2.2}
.fcol li::before{content:"›";color:var(--light);margin-right:6px}
.fcol li.hi{color:var(--blue)}
.news-text{font-size:10px;color:#444;line-height:1.6;width:150px}
.news-field{margin-top:14px;display:flex}
.news-field span{width:128px;height:22px;border:1px solid #ccc;background:var(--white);font-size:10px;color:#aaa;line-height:20px;padding-left:6px}
.news-field b{width:24px;height:22px;background:var(--blue);color:var(--white);text-align:center;line-height:22px;font-size:14px}
.seal{width:48px;height:40px;border-radius:50%;background:#d9b54a}
.cards{display:flex;gap:5px;margin-top:10px}
.cards span{width:38px;height:22px;border:1px solid #ccc;background:var(--white);font-size:7px;font-weight:700;color:#333;text-align:center;line-height:20px;overflow:hidden}

.bottom-bar{left:0;top:2134px;width:1200px;height:51px;background:var(--footer)}
.copyright{left:153px;top:0;line-height:51px;font-size:10px;color:#aaa}
.copyright b{font-weight:400;color:var(--blue)}
.social{left:870px;top:0;line-height:51px;font-size:9.5px;color:#999;display:flex;gap:16px}
.social a:first-child{color:var(--blue)}
</style>
</head>
<body>

<div class="abs promo-bar">ENDS TODAY! TOPS $20, SWEATERS $25, PANTS $29, OUTERWEAR $39 &amp; UP &amp; 40% OFF EVERYTHING ELSE + FREE SHIPPING OVER $50. CLICK FOR DETAILS.</div>

<header class="abs site-header">
  <a class="abs logo"><span class="logo-mark"></span><span class="logo-name">KU Curiosities</span></a>
  <div class="abs prefs"><span>Language: <b>English</b> ▾</span><span>Currency: <b>USD</b> ▾</span></div>
  <nav class="abs account-links"><a>My Account</a><span>|</span><a>Checkout</a><span>|</span><a>Login</a><span>|</span><a>Register</a></nav>
  <nav class="abs main-nav">
    <a class="active">HOME</a><a>SHOP</a><a>THE LATEST</a><a>ABOUT US</a><a>FAQ</a><a>BLOG</a><a>CONTACT US</a>
  </nav>
  <div class="abs search-btn">
    <svg width="28" height="28" viewBox="0 0 28 28"><circle cx="12.5" cy="12.5" r="5.5" fill="none" stroke="#fff" stroke-width="2.2"/><line x1="16.5" y1="16.5" x2="21" y2="21" stroke="#fff" stroke-width="2.4" stroke-linecap="round"/></svg>
  </div>
  <div class="abs cart-btn">
    <svg width="28" height="28" viewBox="0 0 28 28"><path d="M6 8h3l2 9h9l2-7H10" fill="none" stroke="#fff" stroke-width="2" stroke-linejoin="round"/><circle cx="12" cy="21" r="1.6" fill="#fff"/><circle cx="19" cy="21" r="1.6" fill="#fff"/></svg>
  </div>
  <div class="abs cart-count">(0)</div>
</header>

<section class="abs hero" role="img" aria-label="Woman wearing a virtual reality headset">
  <div class="abs hero-title"><span>AMAZE</span> YOUR FRIENDS</div>
  <div class="abs hero-sub">FREE SHIPPING ON ORDERS <span>OVER $50</span></div>
  <a class="abs hero-cta">SHOP NOW</a>
  <div class="abs hero-arrow" style="left:98px">
    <svg width="40" height="40" viewBox="0 0 40 40"><path d="M23 12l-8 8 8 8" fill="none" stroke="#fff" stroke-width="3"/></svg>
  </div>
  <div class="abs hero-arrow" style="left:1064px">
    <svg width="40" height="40" viewBox="0 0 40 40"><path d="M17 12l8 8-8 8" fill="none" stroke="#fff" stroke-width="3"/></svg>
  </div>
</section>

<div class="abs ship-strip">
  <svg class="abs ship-tag" viewBox="0 0 140 70"><path d="M0 0h100l40 35-40 35H0z" fill="#3aa8e0"/><rect x="22" y="20" width="40" height="22" rx="2" fill="#fff"/><path d="M62 26h12l8 8v8H62z" fill="#fff"/><circle cx="34" cy="46" r="5" fill="#fff" stroke="#3aa8e0" stroke-width="2"/><circle cx="72" cy="46" r="5" fill="#fff" stroke="#3aa8e0" stroke-width="2"/><text x="42" y="36" font-family="Open Sans,sans-serif" font-size="10" font-weight="700" fill="#3aa8e0" text-anchor="middle">FREE</text></svg>
  <div class="abs ship-text">FREE SHIPPING ON ORDER OVER $50 OR SOME KIND OF FAKE PROMOTION</div>
</div>

<div class="abs tile" style="left:146px">
  <div class="tile-photo" role="img" aria-label="Man wearing headphones" style="left:130px;width:158px;background:linear-gradient(90deg,#f1ece8 0%,#d8bfae 45%,#8d7464 80%,#5a4d45 100%)"></div>
  <div class="abs tile-1-text">LOREMIPSUM<br>DOLOR SIT 2014</div>
  <a class="abs tile-btn">Shop Now</a>
</div>
<div class="abs tile" style="left:456px;background:#d6e4f5">
  <div class="tile-photo" role="img" aria-label="Woman wearing smart glasses" style="left:120px;width:168px;background:linear-gradient(90deg,#d6e4f5 0%,#dcc3b0 45%,#a37a5f 80%,#7a5640 100%)"></div>
  <div class="abs tile-2-text">NEW<br>COLLECTION<br>FOR 2014</div>
</div>
<div class="abs tile" style="left:764px">
  <div class="tile-photo" role="img" aria-label="Person aiming a handheld launcher gadget" style="left:140px;width:148px;background:linear-gradient(160deg,#f4f4f4 0%,#e6ea9c 40%,#8a8a80 70%,#3a3a3a 100%)"></div>
  <div class="abs tile-3-big">%30<sup>OFF</sup></div>
  <div class="abs tile-3-text">Etiam varius velit in arcu bibendum</div>
</div>

<h2 class="abs section-title">NEW ARRIVALS</h2>
<div class="abs section-rule"></div>
<div class="abs pager" style="left:998px;background:#e6e6e6">
  <svg width="26" height="26" viewBox="0 0 26 26"><path d="M15 8l-5 5 5 5" fill="none" stroke="#fff" stroke-width="2"/></svg>
</div>
<div class="abs pager" style="left:1028px;background:var(--blue)">
  <svg width="26" height="26" viewBox="0 0 26 26"><path d="M11 8l5 5-5 5" fill="none" stroke="#fff" stroke-width="2"/></svg>
</div>

<div class="abs card" style="left:374px;top:980px"><div class="card-photo" role="img" aria-label="Black and orange GPS tracker" style="background:linear-gradient(160deg,#f7f7f7 0%,#d9d9d9 45%,#b9a08c 75%,#f2f2f2 100%)"></div></div>
<div class="abs card" style="left:606px;top:980px"><div class="card-photo" role="img" aria-label="Video eyewear glasses" style="background:linear-gradient(170deg,#f5f5f5 0%,#c9ccd0 50%,#9ea3a8 75%,#f1f1f1 100%)"></div>
  <div class="abs card-flag"></div><div class="abs flag-text" style="left:4px;top:18px">SALES</div></div>
<div class="abs card" style="left:834px;top:980px"><div class="card-photo" role="img" aria-label="Round smart thermostat with orange display" style="background:linear-gradient(160deg,#f5f5f5 0%,#dcdcdc 40%,#e8a07c 65%,#f2f2f2 100%)"></div></div>

<div class="abs card" style="left:146px;top:1265px"><div class="card-photo" role="img" aria-label="Portable music player on a disc" style="background:linear-gradient(160deg,#f3f3f3 0%,#b7bcbf 45%,#6f7478 75%,#ededed 100%)"></div></div>
<div class="abs card" style="left:374px;top:1265px"><div class="card-photo" role="img" aria-label="Smart thermostat with blue display" style="background:linear-gradient(160deg,#f6f6f6 0%,#d8d8d8 40%,#8b9bd6 65%,#f2f2f2 100%)"></div></div>
<div class="abs card" style="left:606px;top:1265px"><div class="card-photo" role="img" aria-label="Solar panel tree charger" style="background:linear-gradient(170deg,#f6f6f6 0%,#a9b0c8 40%,#8c857c 70%,#efefef 100%)"></div></div>
<div class="abs card" style="left:834px;top:1265px"><div class="card-photo" role="img" aria-label="Tabletop tablet game with pink balls" style="background:linear-gradient(160deg,#f6f6f6 0%,#d5dade 45%,#e7a3c4 70%,#f2f2f2 100%)"></div>
  <div class="abs card-flag blue"></div><div class="abs flag-text" style="left:2px;top:18px">30% OFF</div></div>

<div class="abs card-hover">
  <div class="abs" role="img" aria-label="Glowing LED wristwatches" style="left:0;top:0;width:218px;height:200px;background:linear-gradient(135deg,#f4f4f4 0%,#4a4a4a 35%,#7a7f48 55%,#4a4d8a 78%,#ececec 100%)"></div>
  <div class="abs price-badge">$30.00</div>
  <div class="abs hover-name">NEW ORLA PENNINGTON</div>
  <div class="abs stars">★★★☆☆</div>
  <div class="abs hover-rule"></div>
  <div class="abs add-cart">
    <svg width="18" height="16" viewBox="0 0 18 16"><path d="M1 2h3l2 8h8l2-6H5" fill="none" stroke="#3aa8e0" stroke-width="1.8"/><circle cx="7" cy="13.5" r="1.4" fill="#3aa8e0"/><circle cx="13" cy="13.5" r="1.4" fill="#3aa8e0"/></svg>
    Add To Cart
  </div>
  <div class="abs add-links">+ Add To Wishlist<br>+ Add To Compare</div>
</div>

<h3 class="abs col-title" style="left:153px;top:1598px">CHIRPLINE</h3>
<div class="abs tweet" style="top:1634px"><span class="tweet-dot"></span><p class="tweet-body"><b>KU Curiosities</b> dolor sit amet, consec tet uo adi. In interdum aliquet orci vitae.<span class="tweet-time">25 minutes ago</span></p></div>
<div class="abs tweet" style="top:1712px"><span class="tweet-dot"></span><p class="tweet-body"><b>KU Curiosities</b> dolor sit amet, consec tet adi nelit. In interdum aliquet orci.<span class="tweet-time">45 minutes ago</span></p></div>
<div class="abs tweet" style="top:1790px"><span class="tweet-dot"></span><p class="tweet-body"><b>KU Curiosities</b> dolor sit amet, consec tet adi pis In interdum aliquet orci vitae.<span class="tweet-time">one day ago</span></p></div>
<a class="abs follow">Follow us on chirpline &gt;&gt;</a>

<div class="abs vrule" style="left:448px;top:1598px;height:280px"></div>

<h3 class="abs col-title" style="left:485px;top:1598px">CHATTERPAGE</h3>
<div class="abs like-row"><span class="like-btn">Like</span><span>120 people like <b>KU Curiosities</b> Shop</span></div>
<div class="abs" style="left:485px;top:1675px;width:240px;height:1px;background:var(--line)"></div>
<div class="abs" style="left:490px;top:1690px;display:flex;gap:34px">
  <div class="fan"><div class="fan-photo" role="img" aria-label="Member portrait"></div>Alex</div>
  <div class="fan"><div class="fan-photo" role="img" aria-label="Member portrait"></div>Lorem</div>
  <div class="fan"><div class="fan-photo" role="img" aria-label="Member portrait"></div>Ipsut</div>
</div>
<div class="abs" style="left:490px;top:1775px;display:flex;gap:34px">
  <div class="fan"><div class="fan-photo" role="img" aria-label="Member portrait"></div>Alex</div>
  <div class="fan"><div class="fan-photo" role="img" aria-label="Member portrait"></div>Lorem</div>
  <div class="fan"><div class="fan-photo" role="img" aria-label="Member portrait"></div>Ipsut</div>
</div>
<div class="abs" style="left:485px;top:1855px;width:240px;height:1px;background:var(--line)"></div>
<div class="abs plugin"><i></i>Chatterpage social plugin</div>

<div class="abs vrule" style="left:756px;top:1598px;height:280px"></div>

<h3 class="abs col-title" style="left:794px;top:1598px">ABOUT US</h3>
<p class="abs about-text">Lorem ipsum dolor sit amet, consectetur adi pise seo cing elit. Etiam neque velit, blandi sed scele risque quis, vulpu tate vel lorem. Sed luctus, saes pien elem entum viverra pellen tesque, odio turp ultrices sa pien, ut mollis mag na eros vitae.</p>
<div class="abs contact-row" style="top:1756px"><span class="contact-icon"></span><span>68 - Duis Ipsum Street, Bandti<br>Aliquam Vitae. New York</span></div>
<div class="abs contact-row" style="top:1800px"><span class="contact-icon"></span><span>Click Here<br>To Email Us</span></div>
<div class="abs contact-row" style="top:1842px"><span class="contact-icon"></span><span>(+84) 120 555 0147<br>(+84) 93 555 0192</span></div>

<footer class="abs footer">
  <div class="abs fcol" style="left:153px">
    <h4>NEWSLETTER</h4>
    <p class="news-text">Lorem ipsum dolor sit amet, de consectetur adipiscing elit.</p>
    <div class="news-field"><span>Your email...</span><b>+</b></div>
  </div>
  <div class="abs fcol" style="left:331px">
    <h4>INFORMATION</h4>
    <ul><li>About us</li><li>Delivery Information</li><li>Privacy Policy</li><li>Terms &amp; Condition</li></ul>
  </div>
  <div class="abs fcol" style="left:512px">
    <h4>OUR SUPPORT</h4>
    <ul><li>Delivery Information</li><li class="hi">Privacy Policy</li><li>Terms &amp; Condition</li><li>Contact Us</li></ul>
  </div>
  <div class="abs fcol" style="left:690px">
    <h4>OUR SERVICE</h4>
    <ul><li>My Account</li><li>Order History</li><li>Returns</li><li>Site Map</li></ul>
  </div>
  <div class="abs fcol" style="left:870px">
    <h4>PAYMENT</h4>
    <div class="seal" role="img" aria-label="Payment security seal"></div>
    <div class="cards"><span>PayLoop</span><span>Findcard</span><span>Meridian</span><span>Vantra</span></div>
  </div>
</footer>

<div class="abs bottom-bar">
  <div class="abs copyright">Copyright © 2014. <b>KU Curiosities</b>. All rights reserved</div>
  <nav class="abs social"><a>Chatterpage</a><a>Chirpline</a><a>Linkpro</a><a>RSS</a><a>Clipboardly</a></nav>
</div>

</body>
</html>
```